Hedge fund needs power point design for marketing pitch

We need a designer to make our power point pitch more aesthetically appealing to potential clients. We will be marketing our hedge fund to high net worth individuals and financial institutions. The ideal design will look professional and project confidence to our potential clients. We have attached a rough outline of what we have completed so far. We have also attached example cover pages for 2 pitch books produced by our competitors.

Target Market(s)

Financial institutions and wealthy investors

Industry/Entity Type

Finance

Requirements
Must have
• must use our logo and current slides. Must look professional

```html
<!DOCTYPE html>
<html lang="en">
<head>
<meta charset="utf-8">
<title>Alderton Derivatives Fund LP – Pitch Slides</title>
<link href="https://fonts.googleapis.com/css2?family=Ubuntu:wght@400;500&display=swap" rel="stylesheet">
<style>
:root{
  --page:#ececec;
  --gold:#c9962e;
  --gold-light:#f0c84a;
  --gold-text:#c48f27;
  --green:#0f3b2a;
  --ink:#1c1c1c;
  --navy:#10202e;
  --sky-1:#eef4fa;
  --sky-2:#cfe2f1;
  --sky-3:#7fb6dc;
}
*{box-sizing:border-box;margin:0;padding:0}
html,body{width:1200px;height:1200px;overflow:hidden}
body{
  background:radial-gradient(ellipse at center,#fbfbfb 0%,var(--page) 75%);
  font-family:'Ubuntu',sans-serif;color:var(--ink);position:relative;
}
.slide{position:absolute;overflow:hidden;box-shadow:0 4px 8px rgba(0,0,0,.35)}
.bg{position:absolute;inset:0}

/* cover */
.cover{left:36px;top:174px;width:546px;height:408px}
.cover .bg{background:
  radial-gradient(circle at 60px 200px,#3d8fc4 0,#8cc3e6 90px,rgba(255,255,255,0) 170px),
  radial-gradient(ellipse at 80% 10%,#c7dcee 0,rgba(255,255,255,0) 55%),
  linear-gradient(135deg,#dfeaf4 0%,#f4f8fb 50%,#d6e5f2 100%)}
.cover .brand{position:absolute;left:290px;top:76px;width:240px;text-align:center;
  font-size:30px;font-weight:500;letter-spacing:3px;color:var(--navy)}
.cover .rule{position:absolute;left:294px;top:146px;width:228px;height:1px;background:var(--gold)}
.cover .fund{position:absolute;left:195px;top:236px;width:380px;text-align:center;font-size:22px;color:var(--gold-text)}
.cover .conf{position:absolute;left:195px;top:270px;width:380px;text-align:center;font-size:16px;color:var(--ink)}
.cover .date{position:absolute;left:195px;top:377px;width:338px;text-align:center;font-size:10px}

/* disclaimer */
.disclaimer{left:618px;top:174px;width:547px;height:408px}
.disclaimer .bg{background:
  radial-gradient(ellipse at 92% 75%,#e6a533 0,#b8892f 60px,rgba(120,140,170,0) 150px),
  radial-gradient(ellipse at 65% 8%,#e0a640 0,rgba(255,255,255,0) 90px),
  linear-gradient(160deg,#a9c2e2 0%,#6f93c6 55%,#5a7fb8 100%)}
.band{position:absolute;left:0;background:var(--gold);color:#fff;
  box-shadow:2px 2px 3px rgba(0,0,0,.25)}
.disclaimer .band{top:122px;width:208px;height:50px;font-size:32px;padding:4px 0 0 32px}
.disclaimer .note{position:absolute;left:32px;top:186px;font-size:20px;color:var(--ink)}

/* content slides */
.content .bg{background:
  radial-gradient(ellipse at 85% 10%,#c9dced 0,rgba(255,255,255,0) 55%),
  linear-gradient(160deg,var(--sky-2) 0%,var(--sky-1) 45%,#f7fafc 100%)}
.objective{left:26px;top:628px;width:556px;height:418px}
.strategy{left:618px;top:622px;width:565px;height:423px}
.strategy .bg{background:
  linear-gradient(90deg,rgba(255,255,255,0) 55%,rgba(170,195,220,.35) 75%,rgba(255,255,255,0) 95%),
  linear-gradient(160deg,#dbe7f2 0%,#f1f6fa 45%,#f7fafc 100%)}
.mini-brand{position:absolute;top:30px;right:12px;font-size:13px;font-weight:500;letter-spacing:1px;color:var(--navy)}
.objective .band{top:30px;width:374px;height:51px;font-size:34px;padding:6px 0 0 39px}
.strategy .band{top:27px;width:387px;height:51px;font-size:34px;padding:4px 0 0 34px}
.footer{position:absolute;left:0;right:0;bottom:0}
.footer .gilt{height:30px;background:linear-gradient(90deg,var(--gold) 0%,#d9a830 30%,var(--gold-light) 50%,#d9a830 70%,var(--gold) 100%)}
.footer .base{height:10px;background:var(--green)}

ul.points{position:absolute;list-style:none}
ul.points > li{position:relative;padding-left:20px}
ul.points > li::before{content:"•";position:absolute;left:0}
ul.sub{list-style:none}
ul.sub li{position:relative;padding-left:18px}
ul.sub li::before{content:"–";position:absolute;left:0}

.objective ul.points{left:38px;top:104px;width:480px;font-size:24px;line-height:29px}
.objective ul.points > li{margin-bottom:2px}
.objective ul.sub{font-size:21px;line-height:31px;margin:2px 0 2px}
.objective ul.sub li{padding-left:18px}

.strategy ul.points{left:34px;top:104px;width:500px;font-size:17px;line-height:20px}
.strategy ul.points > li{margin-bottom:4px}
.strategy ul.points > li::before{font-size:14px}
.strategy ul.sub{font-size:15px;line-height:23px;margin:1px 0 0 6px}
</style>
</head>
<body>

<section class="slide cover">
  <div class="bg" role="img" aria-label="Glowing globe and world map with network light trails in soft blue"></div>
  <div class="brand">ALDERTON</div>
  <div class="rule"></div>
  <div class="fund">Alderton Derivatives Fund LP</div>
  <div class="conf">Confidential</div>
  <div class="date">April 2016</div>
</section>

<section class="slide disclaimer">
  <div class="bg" role="img" aria-label="Close-up photo of golden balance scales against a blue background"></div>
  <div class="band">Disclaimer</div>
  <p class="note">Get legal counsel on this</p>
</section>

<section class="slide content objective">
  <div class="bg" role="img" aria-label="Faint world map and globe in pale blue"></div>
  <div class="mini-brand">ALDERTON</div>
  <h2 class="band" style="font-weight:400">Investment Objective</h2>
  <ul class="points">
    <li>Profit from inefficiencies in equity and index options markets
      <ul class="sub">
        <li>Buy options that are underpriced</li>
        <li>Sell options that are overpriced</li>
      </ul>
    </li>
    <li>Achieve outsized and consistent returns by maintaining a small and nimble fund that can exploit price inefficiencies and move in and out of trades quickly</li>
  </ul>
  <div class="footer"><div class="gilt"></div><div class="base"></div></div>
</section>

<section class="slide content strategy">
  <div class="bg" role="img" aria-label="Faint glass office tower facade in pale blue"></div>
  <div class="mini-brand">ALDERTON</div>
  <h2 class="band" style="font-weight:400">Investment Strategy</h2>
  <ul class="points">
    <li>Strategy derived from a dynamic optimization problem that maximizes returns within a given risk constraint.</li>
    <li>Parameters/assumptions
      <ul class="sub">
        <li>Assume liquid markets</li>
        <li>Assume a price discount/premium on each trade (5-10%)</li>
      </ul>
    </li>
    <li>Solution - the optimization problem tells us:
      <ul class="sub">
        <li>When to buy or sell contracts</li>
        <li>Which contracts to buy or sell</li>
        <li>How many contracts to buy or sell</li>
      </ul>
    </li>
    <li>We make trades based on these solutions while hitting the price discount/premium offered by the market.</li>
  </ul>
  <div class="footer"><div class="gilt"></div><div class="base"></div></div>
</section>

</body>
</html>
```